Music Quizz Application

Hello,

I want a new design for my Blind test (music quizz) application on Velphon. You will find attached the images I want to replace. I need something with the same element (menu / song title) but with a different look!

Same, new icon, you have carte blanche to this one.

I am looking for something fresh…. I'm looking for something with a real artistic choice, contrast, colours, etc.

As a marketing screenshot, I want something classic, you'll find an example attached, feel free to innovate.

To sum-up :

- One new view for my App
- One new icon
- One marketing screenshot

screen resolution :
640×960
icon resolution :
1024x1024

Target Market(s)

15-30 years

Industry/Entity Type

Marketing

```html
<!DOCTYPE html>
<html lang="en">
<head>
<meta charset="utf-8">
<title>Tune Hunt – Score Help View</title>
<link href="https://fonts.googleapis.com/css2?family=Arimo:wght@400;700&family=Open+Sans:ital,wght@0,400;0,600;1,600&display=swap" rel="stylesheet">
<style>
  :root {
    --page-bg: #ffffff;
    --status-bg: #0a0a0a;
    --status-text: #e8e8e8;
    --screen-blue: #3f6fe0;
    --screen-blue-deep: #2a4fc4;
    --screen-blue-light: #6b93f0;
    --title-red: #d8141a;
    --mark-dark: #1c1c1e;
    --bar-top: #f4f4f6;
    --bar-mid: #a9aeb8;
    --bar-bottom: #5d6370;
    --bar-text: #ffffff;
    --panel-top: #ffffff;
    --panel-bottom: #9aa1ad;
    --panel-text: #1a1d24;
    --hint-text: #fff6c8;
  }
  * { box-sizing: border-box; margin: 0; padding: 0; }
  html, body {
    width: 1200px; height: 610px; overflow: hidden;
    background: var(--page-bg);
  }
  .stage {
    width: 1200px; height: 610px;
    display: flex; align-items: center; justify-content: center;
  }
  .app-screen {
    position: relative;
    width: 380px; height: 570px;
    overflow: hidden;
    background:
      radial-gradient(ellipse at 30% 20%, var(--screen-blue-light) 0%, transparent 55%),
      radial-gradient(ellipse at 80% 85%, var(--screen-blue-deep) 0%, transparent 60%),
      var(--screen-blue);
  }
  .status-bar {
    position: absolute; left: 0; top: 0; width: 100%; height: 29px;
    background: var(--status-bg);
    color: var(--status-text);
    font: 600 12px "Open Sans", sans-serif;
    display: flex; align-items: center; justify-content: space-between;
    padding: 0 10px;
  }
  .status-bar .battery { display: flex; align-items: center; gap: 4px; }
  .app-header {
    position: absolute; left: 30px; top: 70px; width: 320px; height: 100px;
    display: flex; align-items: center; justify-content: center; gap: 18px;
  }
  .brand-dot {
    width: 70px; height: 70px; border-radius: 50%;
    background: var(--mark-dark);
    flex: none;
  }
  .app-title {
    font: 700 34px/1 "Arimo", sans-serif;
    color: var(--title-red);
    white-space: nowrap;
  }
  .glossy-bar {
    position: absolute;
    height: 30px;
    border-radius: 6px;
    background: linear-gradient(to bottom, var(--bar-top) 0%, var(--bar-mid) 50%, var(--bar-bottom) 100%);
    box-shadow: 0 2px 4px rgba(0,0,0,0.45);
    color: var(--bar-text);
    font: 700 16px "Arimo", sans-serif;
    text-shadow: 0 1px 2px rgba(0,0,0,0.7);
    display: flex; align-items: center; justify-content: center;
  }
  .question-bar { left: 36px; top: 192px; width: 312px; }
  .answer-bar   { left: 44px; top: 236px; width: 296px; }
  .score-panel {
    position: absolute; left: 42px; top: 281px; width: 306px; height: 188px;
    border-radius: 12px;
    background: linear-gradient(to bottom, var(--panel-top) 0%, #e2e4e9 45%, var(--panel-bottom) 100%);
    box-shadow: 0 3px 6px rgba(0,0,0,0.5);
    padding: 12px 14px;
    color: var(--panel-text);
    font: 400 14.5px/1.3 "Arimo", sans-serif;
  }
  .score-panel .sign-off { margin-top: 14px; }
  .dismiss-hint {
    position: absolute; left: 0; top: 494px; width: 100%;
    text-align: center;
    color: var(--hint-text);
    font: italic 600 12px "Open Sans", sans-serif;
  }
</style>
</head>
<body>
<main class="stage">
  <section class="app-screen">
    <header class="status-bar">
      <span class="carrier">Novo&nbsp;&nbsp;3G</span>
      <span class="clock">12:14</span>
      <span class="battery">89 %
        <svg width="22" height="11" viewBox="0 0 22 11" aria-hidden="true">
          <rect x="0.5" y="0.5" width="18" height="10" rx="1.5" fill="none" stroke="#e8e8e8"/>
          <rect x="2" y="2" width="14" height="7" fill="#e8e8e8"/>
          <rect x="19" y="3.5" width="2" height="4" fill="#e8e8e8"/>
        </svg>
      </span>
    </header>

    <div class="app-header">
      <span class="brand-dot" aria-hidden="true"></span>
      <h1 class="app-title">Tune Hunt</h1>
    </div>

    <div class="glossy-bar question-bar">HOw is the score calculated?</div>
    <div class="glossy-bar answer-bar">Points are awarded as follows:</div>

    <div class="score-panel">
      <p>-1 for each incorrect answer,<br>
      +5 or +10 for each correct answer (depended on whether your game features 5 or 10 possible answer),<br>
      1 point is deducated for every 10 seconds thatpass.</p>
      <p class="sign-off">Good luck :)</p>
    </div>

    <p class="dismiss-hint">Tap Tap to dismiss the window</p>
  </section>
</main>
</body>
</html>
```